Flyer for Addiction program

Hi There,There are two parts to this project.1. A double-sided flyer for my next 5-day treatment program for addictions and family trauma.2. A one-page cover for the front of the course folders to match the above flyer?I have put together an information folder. Here is the boxfolio link;https://www.boxfolio.com/sh/jn7lkly6wcqphpt/AACmad0pag08NeuT2pM27USPa?dl=0Included in the information folder is;1. Copy2. Selection of images3. Logos and Brand identity kit4. Examples of past flyers and folder coverPlease don't hesitate to contact me if you have any questions.RegardsRebecca

Colors

Designer to choose colors to be used in the design.

Requirements
Must have
• 2 pages flyer please.
• Contemporary / fresh design

```html
<!DOCTYPE html>
<html lang="en">
<head>
<meta charset="utf-8">
<title>Breaking the Family Trance – 5 day program flyer</title>
<link href="https://fonts.googleapis.com/css2?family=Oswald:wght@400;500;600&family=Open+Sans:ital,wght@0,400;0,600;0,700;1,400;1,600&display=swap" rel="stylesheet">
<style>
:root{
  --navy:#1b2a3f;
  --navy-veil:rgba(27,42,63,.78);
  --white:#ffffff;
  --ink:#1e2530;
  --grey:#d7dade;
  --stone:#b9b3a9;
  --gold-1:#f6e6b8;
  --gold-2:#d9b877;
  --page-bg:#eceae6;
}
*{box-sizing:border-box;margin:0;padding:0}
html,body{width:1200px;height:1200px;overflow:hidden;background:var(--page-bg);font-family:"Open Sans",Arial,sans-serif;color:var(--ink)}
.page{position:absolute;top:204px;width:560px;height:792px;overflow:hidden;box-shadow:0 6px 18px rgba(0,0,0,.18)}
.front{left:30px}
.back{left:610px;background:var(--white)}

/* FRONT */
.front-photo{position:absolute;inset:0;background:radial-gradient(ellipse at 72% 55%,#5a4a44 0%,#6f7a72 30%,#9aa79d 60%,#c9d0c8 100%)}
.front-panel{position:absolute;left:32px;top:0;width:296px;height:792px;background:var(--navy-veil)}
.brand{position:absolute;left:0;right:0;top:52px;text-align:center;color:var(--stone);font:400 19px/1 "Open Sans",sans-serif;letter-spacing:5px}
.brand-dot{display:block;width:46px;height:46px;border-radius:50%;background:var(--stone);margin:0 auto 22px}
.title-1{position:absolute;left:22px;top:178px;color:var(--white);font:500 48px/1 "Oswald",sans-serif;letter-spacing:-.5px}
.title-2{position:absolute;left:22px;top:240px;background:var(--white);color:var(--navy);font:500 40px/1 "Oswald",sans-serif;padding:8px 12px 10px}
.title-3{position:absolute;left:36px;top:316px;border:1px solid var(--white);color:var(--white);font:500 30px/1 "Oswald",sans-serif;padding:8px 18px 10px}
.quote{position:absolute;left:30px;top:490px;width:256px;color:var(--white);font:italic 400 12.5px/1.45 "Open Sans",sans-serif;padding:0 26px 0 22px}
.quote .mark{position:absolute;font:700 28px/1 "Oswald",sans-serif}
.quote .open{left:-4px;top:-6px}
.quote .close{right:4px;bottom:-24px}
.attribution{position:absolute;left:150px;top:584px;color:var(--white);font:600 12px/1 "Open Sans",sans-serif}
.intro{position:absolute;left:40px;top:640px;width:245px;color:var(--white);font:400 12.5px/1.4 "Open Sans",sans-serif}
.intro em{font-weight:600}
.rule{position:absolute;left:120px;top:760px;width:170px;height:1px;background:var(--white)}

/* BACK */
.hero{position:absolute;left:0;top:0;width:560px;height:170px;background:linear-gradient(180deg,var(--gold-1),var(--gold-2))}
.hero-silhouettes{position:absolute;left:250px;top:20px;width:300px;height:150px;background:linear-gradient(90deg,rgba(40,30,20,0) 0%,rgba(40,30,20,.35) 60%,rgba(40,30,20,.55) 100%)}
.hero-copy{position:absolute;left:26px;top:30px;width:230px;font:600 9.3px/1.35 "Open Sans",sans-serif;color:var(--ink);text-align:justify}
.info{position:absolute;left:0;top:170px;width:560px;height:350px;background:var(--navy);color:var(--white)}
.col{position:absolute;top:14px}
.col-left{left:18px;width:252px}
.col-right{left:292px;width:252px}
.divider{position:absolute;left:280px;top:0;width:1px;height:350px;background:rgba(255,255,255,.7)}
.col h3{font:400 10.5px/1 "Open Sans",sans-serif;text-transform:uppercase;margin-bottom:10px}
.col p,.col li{font-size:6.2px;line-height:1.35}
.col ul{list-style:none;margin-top:6px}
.col li{margin-bottom:8px;padding-left:8px;position:relative}
.col li::before{content:"»";position:absolute;left:0;font-weight:700}
.col .lead{font-weight:700;margin-top:4px}
.col .closing{position:absolute;top:284px;width:252px}
.details{position:absolute;left:14px;top:534px;width:250px}
.details h3,.enrol h3,.inclusions h3{font:500 11px/1 "Oswald",sans-serif;text-transform:uppercase;margin-bottom:8px}
.schedule{width:100%;border-collapse:collapse;font-size:8.5px}
.schedule td{padding:4px 6px;font-weight:600}
.schedule tr:nth-child(odd){background:var(--grey)}
.inclusions{position:absolute;left:14px;top:660px;width:250px}
.inclusions p{font-size:7.2px;line-height:1.4}
.investment{position:absolute;left:14px;top:726px;font:500 11px/1 "Oswald",sans-serif;text-transform:uppercase}
.investment strong{font:600 32px/1 "Oswald",sans-serif;vertical-align:-6px;margin:0 3px}
.investment span{text-transform:none;font-size:12px}
.enrol{position:absolute;left:290px;top:534px;width:254px}
.enrol .close-date{font-size:8.5px;font-weight:600;margin-bottom:8px}
.book-box{background:var(--navy);color:var(--white);font-size:9px;font-weight:600;text-align:center;padding:7px 10px;line-height:1.35;border:2px dashed var(--white);outline:2px solid var(--navy)}
.terms{margin-top:10px}
.terms h4{font-size:8px;font-weight:700;text-transform:uppercase}
.terms p{font-size:7.4px;line-height:1.35;text-align:justify}
.company{position:absolute;left:290px;top:706px;width:254px;font:400 9px/1.7 "Oswald",sans-serif}
.company .name{font-size:12px;font-weight:500}
.company-mark{position:absolute;right:18px;top:-10px;width:32px;height:32px;border-radius:50%;background:var(--stone)}
.grass{position:absolute;left:0;bottom:0;width:280px;height:56px;background:linear-gradient(180deg,rgba(217,184,119,0),#d4ad62 70%,#b48a3e)}
</style>
</head>
<body>

<section class="page front">
  <div class="front-photo" role="img" aria-label="Photograph of a woman sitting among forest undergrowth holding her head"></div>
  <div class="front-panel">
    <div class="brand"><span class="brand-dot"></span>LUMEN GROUP</div>
    <h1 class="title-1">Breaking the</h1>
    <div class="title-2">Family Trance</div>
    <div class="title-3">5 day program</div>
    <blockquote class="quote">
      <span class="mark open">“</span>If you cannot get rid of the family skeleton, you may as well make it dance<span class="mark close">”</span>
    </blockquote>
    <p class="attribution">-Edmund Hale</p>
    <p class="intro"><em>“Breaking the Family Trance”</em> and breaking out of your adapted family roles is one of the most important things you can do to feel happy with yourself and in your relationships.</p>
    <div class="rule"></div>
  </div>
</section>

<section class="page back">
  <div class="hero" role="img" aria-label="Sunset photograph with silhouettes of a family and a child with balloons"></div>
  <div class="hero-silhouettes" role="img" aria-label="Silhouetted family figures against the sky"></div>
  <p class="hero-copy">Participating in Breaking the Family Trance will help you uncover the unconscious psychological defences, which create destructive habits and behaviour patterns that keep you stuck; recycling the same unfulfilling relationships, circumstances and patterns in your life.</p>

  <div class="info">
    <div class="col col-left">
      <h3>How do you know if you need to break free?</h3>
      <p>Consider the following questions:</p>
      <ul>
        <li>Do you struggle to meet your own needs and wants, placing friends and family first?</li>
        <li>Do you adapt to fit in, be liked or accepted?</li>
        <li>Are you the one who is overly responsible for others or at work?</li>
        <li>Are you an over achiever only to find you are never satisfied with the end result?</li>
        <li>Do you suffer from repetitive, frustrating situations and unhealthy behaviours in your personal and professional relationships?</li>
        <li>Are you “the one” who listens to others download their problems?</li>
        <li>Do you feel uncomfortable asking others for help?</li>
        <li>Are you tired of being invisible?</li>
        <li>Do you find yourself feeling compelled to distract others, or use humour to ease emotional tension?</li>
        <li>Are you tired of searching for what you can DO or acquire to feel happy and satisfied?</li>
      </ul>
      <p class="lead">Maybe it’s time to think about what you can undo!</p>
      <p>If you answered yes to any of the above questions, it’s likely that you are carrying a family legacy and a family role from your formative years that does not belong to you. If you seem to be sabotaging your success these roles and unconscious family patterns may well be getting in the way of your happiness and well being.</p>
    </div>
    <div class="divider"></div>
    <div class="col col-right">
      <h3>Program benefits</h3>
      <p>During the program you will learn how to:</p>
      <ul>
        <li>Recognise the ways you adapt, so you can undo the false you and unleash the true you.</li>
        <li>Identify what you need to do for yourself to stop destructive behaviour patterns.</li>
        <li>Uncover important values that will bring you deep fulfilment.</li>
        <li>Speak up and be heard</li>
        <li>Be present and be seen.</li>
        <li>Ask for help without feeling too embarrassed or vulnerable</li>
        <li>Manage your emotions, rather than everyone else’s.</li>
        <li>Share responsibility with others and have more equal relationships.</li>
        <li>Discover what you really need and want, and learn the strategy of creating a vision</li>
        <li>Discover what your true needs are and work on getting them met</li>
      </ul>
      <p class="closing">History doesn’t have to repeat itself. The program is specifically designed for those of you who are ready to address the CORE ISSUES that prevent you from experiencing success, freedom and deep fulfilment in your relationships and in your life.</p>
    </div>
  </div>

  <div class="details">
    <h3>Program details</h3>
    <table class="schedule">
      <tr><td>Thursday</td><td>24th January</td><td>9:00am - 5:00pm</td></tr>
      <tr><td>Friday</td><td>25th January</td><td>9:00am - 5:00pm</td></tr>
      <tr><td>Saturday</td><td>26th January</td><td>9:00am - 5:00pm</td></tr>
      <tr><td>Sunday</td><td>27th January</td><td>9:00am - 5:00pm</td></tr>
      <tr><td>Monday</td><td>28th January</td><td>9:00am - 5:00pm</td></tr>
    </table>
  </div>
  <div class="inclusions">
    <h3>Inclusions</h3>
    <p>A pre-program phone consult. Relevant online diagnostic surveys. Integrated Equine Assisted Psychotherapy. Art Therapy Piece. All course materials (notebook, writing materials). Morning and afternoon tea daily + light lunch</p>
  </div>
  <p class="investment">Investments : <strong>$2400</strong> <span>including GST</span></p>

  <div class="enrol">
    <h3>Enrolment process</h3>
    <p class="close-date">Enrolments close Friday, 18th January 2019</p>
    <div class="book-box">To book your place, register your interest or find out more about this program please call Marion 0400 555 019.</div>
    <div class="terms">
      <h4>Terms &amp; conditions</h4>
      <p>A non-refundable deposit of $800 is required to hold your place.<br>Full payment is required by Friday 18th January 2019. Charge card transactions incur a 3.3% merchant fee, other credit cards 2.5%.<br>Debit card facility available.</p>
    </div>
  </div>
  <div class="company">
    <span class="company-mark"></span>
    <div class="name">The Lumen Group Pty Ltd.</div>
    <div>ABN 00 000 000 000 Fernbrook Lane, Kurrajong NSW 2758</div>
    <div>Phone: 0400 555 019</div>
    <div>Email: marion@lumengroup.example</div>
  </div>
  <div class="grass" role="img" aria-label="Golden grass photograph strip"></div>
</section>

</body>
</html>
```